Twitter Bootstrap Website Design (Gaming Themed)

I need a website designed using Twitter Bootstrap for a Rewards website. We'd like to see a gaming based design as the site will cater mostly to gamers.
This is a rewards site similar to sites like LootPenny
I only need the HTML/CSS design.
I need these pages:
1. Homepage for non-logged in users which will also have a sign up form
2. Homepage for logged in users
3. Profile Page
4. Rewards page which will display items that the user can redeem
a) A drop-down to sort by item category
5. Rewards page item details which will display a single item's details
6. About, FAQ, Terms Of Service Pages
Target Market(s)
13 to 30 year old gamers
Mostly males
Industry/Entity Type
It Service
Look and feel

```html
<!DOCTYPE html>
<html lang="en">
<head>
<meta charset="utf-8">
<title>Kestrel Gaming</title>
<link rel="stylesheet" href="https://fonts.googleapis.com/css2?family=PT+Sans:wght@400;700&family=PT+Sans+Narrow:wght@400;700&display=swap">
<style>
  :root {
    --header-bg: #0f2138;
    --hero-deep: #07162a;
    --hero-mid: #1a3c63;
    --hero-glow: #5d8fbd;
    --panel-bg: rgba(18, 40, 66, 0.92);
    --input-bg: #eceef0;
    --input-text: #3a3a3a;
    --accent-orange: #f7a10a;
    --accent-orange-dark: #f08a00;
    --accent-cyan: #2ec3e8;
    --accent-cyan-dark: #1aa8d6;
    --text-white: #ffffff;
    --text-soft: #d5dde6;
    --text-body: #c9c9c9;
    --section-black: #000000;
    --footer-bg: #222222;
    --footer-link: #9a9a9a;
    --bottom-bg: #2b2b2b;
    --bottom-text: #767676;
  }
  * { box-sizing: border-box; margin: 0; padding: 0; }
  html, body { width: 1136px; height: 1200px; overflow: hidden; }
  body { font-family: "PT Sans", sans-serif; background: var(--section-black); position: relative; color: var(--text-white); }

  .site-header { position: absolute; left: 0; top: 0; width: 1136px; height: 106px; background: linear-gradient(180deg, #0c1c31 0%, var(--header-bg) 100%); z-index: 2; }
  .brand { position: absolute; left: 90px; top: 30px; font-family: "PT Sans", sans-serif; font-weight: 700; font-size: 38px; letter-spacing: 1px; color: var(--text-white); text-transform: uppercase; }
  .main-nav { position: absolute; left: 560px; top: 50px; display: flex; align-items: center; font-family: "PT Sans Narrow", sans-serif; font-size: 18px; color: var(--text-soft); }
  .main-nav a { color: inherit; text-decoration: none; }
  .main-nav .sep { width: 1px; height: 15px; background: #5d7895; margin: 0 16px; }
  .login-btn { position: absolute; left: 941px; top: 44px; width: 82px; height: 31px; border: 1px solid #557896; border-radius: 3px; background: linear-gradient(180deg, #2b4b6d, #1a3452); color: var(--text-soft); font-family: "PT Sans Narrow", sans-serif; font-size: 15px; display: flex; align-items: center; justify-content: center; }

  .hero { position: absolute; left: 0; top: 106px; width: 1136px; height: 474px; }
  .hero-art { position: absolute; inset: 0; background:
      radial-gradient(ellipse 320px 260px at 860px 170px, rgba(120,160,200,0.55), transparent 70%),
      radial-gradient(ellipse 420px 300px at 560px 240px, rgba(40,80,125,0.6), transparent 70%),
      linear-gradient(180deg, var(--hero-mid) 0%, var(--hero-deep) 85%, #0a0f18 100%); }
  .hero-copy { position: absolute; left: 102px; top: 126px; width: 560px; }
  .hero-title { font-size: 47px; font-weight: 400; line-height: 1.1; }
  .hero-subtitle { font-size: 34px; font-weight: 400; line-height: 1.2; margin-top: 2px; }
  .hero-text { font-size: 13.5px; line-height: 21px; color: var(--text-soft); margin-top: 10px; width: 440px; margin-left: 2px; }
  .btn-learn { position: absolute; left: 2px; top: 274px; width: 118px; height: 32px; border-radius: 3px; background: linear-gradient(180deg, var(--accent-orange), var(--accent-orange-dark)); font-family: "PT Sans Narrow", sans-serif; font-size: 14.5px; font-weight: 700; display: flex; align-items: center; justify-content: center; text-transform: uppercase; }

  .signup-panel { position: absolute; left: 707px; top: 69px; width: 304px; height: 350px; background: var(--panel-bg); border-radius: 3px; }
  .signup-title { position: absolute; left: 18px; top: 18px; width: 268px; text-align: center; font-family: "PT Sans Narrow", sans-serif; font-size: 27px; font-weight: 400; padding-bottom: 8px; border-bottom: 1px solid #3c5773; }
  .field { position: absolute; left: 23px; width: 256px; height: 33px; background: var(--input-bg); border-radius: 2px; color: var(--input-text); font-size: 14px; padding-left: 12px; display: flex; align-items: center; }
  .code-note { position: absolute; right: 28px; top: 260px; font-size: 11.5px; color: var(--text-soft); }
  .btn-start { position: absolute; left: 27px; top: 288px; width: 245px; height: 38px; border-radius: 2px; background: linear-gradient(180deg, #45d2f2, var(--accent-cyan-dark)); font-family: "PT Sans Narrow", sans-serif; font-size: 19px; display: flex; align-items: center; justify-content: center; }

  .welcome { position: absolute; left: 0; top: 580px; width: 1136px; height: 305px; background: var(--section-black); }
  .welcome-title { position: absolute; left: 96px; top: 70px; font-size: 28px; font-weight: 400; }
  .welcome-text { position: absolute; left: 98px; top: 113px; width: 560px; font-size: 13.6px; line-height: 20.8px; color: var(--text-body); }
  .video-thumb { position: absolute; left: 731px; top: 61px; width: 291px; height: 187px; background: linear-gradient(120deg, #c8751f 0%, #3b2414 45%, #9a7a5c 75%, #d8cdbd 100%); }
  .video-thumb svg { position: absolute; left: 121px; top: 69px; }

  .site-footer { position: absolute; left: 0; top: 885px; width: 1136px; height: 254px; background: var(--footer-bg); border-top: 1px solid #3a3a3a; }
  .footer-col { position: absolute; top: 36px; }
  .footer-col h3 { font-size: 20px; font-weight: 400; color: var(--text-white); margin-bottom: 4px; }
  .footer-col ul { list-style: none; }
  .footer-col li { font-size: 14px; line-height: 26.4px; color: var(--footer-link); }

  .bottom-bar { position: absolute; left: 0; top: 1139px; width: 1136px; height: 61px; background: var(--bottom-bg); }
  .copyright { position: absolute; left: 104px; top: 22px; font-size: 11.5px; color: var(--bottom-text); }
</style>
</head>
<body>
  <header class="site-header">
    <div class="brand">Kestrel Gaming</div>
    <nav class="main-nav">
      <a href="#">MAIN</a><span class="sep"></span>
      <a href="#">ABOUT US</a><span class="sep"></span>
      <a href="#">CONTACT</a><span class="sep"></span>
      <a href="#">SIGN UP</a>
    </nav>
    <div class="login-btn">LOGIN</div>
  </header>

  <section class="hero">
    <div class="hero-art" role="img" aria-label="Dark blue fantasy game artwork of an armoured warrior king in icy mist"></div>
    <div class="hero-copy">
      <h1 class="hero-title">Duis tincidunt lectus quis</h1>
      <h2 class="hero-subtitle">Maecenas placerat consequat</h2>
      <p class="hero-text">Mauris vel lacus vitae felis vestibulum volutpat. Etiam est nunc, venenatis in, tristique eu, imperdiet ac, nisl. Cum sociis natoque penatibus et magnis dis parturient montes, nascetur ridiculus mus.</p>
      <div class="btn-learn">Learn More</div>
    </div>

    <form class="signup-panel">
      <h2 class="signup-title">MEMBER SIGN UP</h2>
      <div class="field" style="top:90px">Full name</div>
      <div class="field" style="top:134px">Email address</div>
      <div class="field" style="top:178px">Password</div>
      <div class="field" style="top:223px">Phone no.</div>
      <div class="code-note">I have a sign up code (optional)</div>
      <div class="btn-start">Free! Get Started</div>
    </form>
  </section>

  <section class="welcome">
    <h2 class="welcome-title">Welcome to Our Website Mainpage..</h2>
    <p class="welcome-text">Vivamus porttitor, g, purus nisi eleifend libero, a tempus libero lectus feugiat felis. Morbi diam mauris, viverra in, gravida eu, mattis in, ante. Morbi eget arcu. Morbi porta, libero id ullamcorper nonummy, nibh ligula pulvinar metus, eget consectetuer augue nisi quis lacus. Ut ac mi quis lacus mollis aliquam. Curabitur iaculis tempus eros. Curabitur vel mi sit amet magna malesuada ultrices. Ut nisi erat, fermentum vel, congue id, euismod in, elit. Fusce ultricies, orci ac feugiat suscipit, leo massa sodales velit, et scelerisque mi tortor at ipsum.</p>
    <div class="video-thumb" role="img" aria-label="Video preview showing fiery game artwork with a hero character">
      <svg width="48" height="48" viewBox="0 0 48 48" aria-hidden="true">
        <circle cx="24" cy="24" r="22" fill="#1c1c1c" stroke="#ffffff" stroke-width="3"/>
        <path d="M19 15 L33 24 L19 33 Z" fill="#ffffff"/>
      </svg>
    </div>
  </section>

  <footer class="site-footer">
    <div class="footer-col" style="left:104px">
      <h3>Quick Links</h3>
      <ul><li>Curabitur vel mi</li><li>Sit amet magna</li><li>malesuada ultrices</li><li>Ut nisi erat fermentum</li><li>Cel congue&nbsp; euismod</li></ul>
    </div>
    <div class="footer-col" style="left:302px">
      <h3>Sub Links</h3>
      <ul><li>Curabitur vel mi</li><li>Sit amet magna</li><li>malesuada ultrices</li><li>Ut nisi erat fermentum</li><li>Cel congue&nbsp; euismod</li></ul>
    </div>
    <div class="footer-col" style="left:498px">
      <h3>Sub Links</h3>
      <ul><li>Curabitur vel mi</li><li>malesuada ultrices</li><li>Ut nisi erat fermentum</li><li>Cel congue&nbsp; euismod</li></ul>
    </div>
    <div class="footer-col" style="left:694px">
      <h3>Resources</h3>
      <ul><li>Curabitur vel mi</li><li>Sit amet magna</li><li>malesuada ultrices</li><li>Ut nisi erat fermentum</li><li>Cel congue&nbsp; euismod</li></ul>
    </div>
  </footer>

  <div class="bottom-bar">
    <p class="copyright">© 2013 Company Name.&nbsp; All right reserved.&nbsp; Term of Use</p>
  </div>
</body>
</html>
```